Halvern Assay Advisors.

Molecular Technology Consulting. Feasibility, Evaluation and Validation of ISH/IHC and Imaging Applications.

Industry/Entity Type

Consulting

Contact Information for Business Card

Halvern Assay Advisors
Cell: 614 905-7738
Dale Morrow
dmorrow4817@quillpost.net

```html
<!DOCTYPE html>
<html lang="en">
<head>
<meta charset="utf-8">
<title>Halvern Assay Advisors – Business Card</title>
<link href="https://fonts.googleapis.com/css2?family=Courier+Prime:wght@400;700&display=swap" rel="stylesheet">
<style>
  :root {
    --stage: #4f4f4f;
    --brand-blue: #0070b8;
    --card-white: #ffffff;
    --ink: #333333;
    --rule: rgba(255, 255, 255, 0.75);
  }
  html, body {
    margin: 0;
    padding: 0;
    width: 1200px;
    height: 1000px;
    overflow: hidden;
    background: var(--stage);
  }
  .canvas {
    position: relative;
    width: 1200px;
    height: 1000px;
    font-family: "Courier Prime", "Courier New", monospace;
  }
  .card {
    position: absolute;
    left: 266px;
    width: 763px;
    height: 435px;
  }
  .card--front {
    top: 28px;
    background: var(--brand-blue);
    color: var(--card-white);
  }
  .card--back {
    top: 530px;
    height: 436px;
    background: var(--card-white);
    color: var(--ink);
  }
  .brand-dot {
    position: absolute;
    left: 62px;
    top: 191px;
    width: 50px;
    height: 50px;
    border-radius: 50%;
    background: var(--card-white);
  }
  .brand-divider {
    position: absolute;
    left: 163px;
    top: 141px;
    width: 2px;
    height: 147px;
    background: var(--rule);
  }
  .brand-name {
    position: absolute;
    left: 191px;
    top: 186px;
    margin: 0;
    font-size: 14px;
    font-weight: 400;
    line-height: 23.5px;
    letter-spacing: 0.9px;
    text-transform: uppercase;
  }
  .card-details {
    position: absolute;
    left: 38px;
    top: 31px;
    margin: 0;
    font-size: 15.8px;
    line-height: 21px;
    text-transform: uppercase;
  }
  .card-details p { margin: 0; }
  .card-details .person { font-weight: 700; }
  .card-details .contact {
    text-transform: none;
    display: flex;
  }
  .card-details .contact .email { width: 297px; }
  .corner-name {
    position: absolute;
    right: 38px;
    bottom: 34px;
    margin: 0;
    font-size: 15px;
    line-height: 20px;
    text-align: right;
    text-transform: uppercase;
    color: var(--brand-blue);
  }
</style>
</head>
<body>
<main class="canvas">
  <section class="card card--front" aria-label="Card front">
    <div class="brand-dot"></div>
    <div class="brand-divider"></div>
    <h1 class="brand-name">Halvern<br>Assay<br>Advisors</h1>
  </section>

  <section class="card card--back" aria-label="Card back">
    <div class="card-details">
      <p>Halvern Assay Advisors</p>
      <p>Feasibility, evaluation and validation of ISH/IHC and imaging applications.</p>
      <p class="person">Dale Morrow: Molecular Technology Consultant</p>
      <p class="contact"><span class="email">email: dmorrow4817@quillpost.net</span><span class="tel">tel: 614 905-7738</span></p>
    </div>
    <p class="corner-name">Halvern<br>Assay<br>Advisors</p>
  </section>
</main>
</body>
</html>
```